Business card update

Opening a subsidiary of my company in the USA and need to update my logo.
Updates

I made a mistake on my briefing. It's only the business card. Thanks for alerting me on the mistake.

All the best

Gustavo

Target Market(s)

We are an Executive Search company and our target audience are executives in large corporations.

Industry/Entity Type

Business

Requirements
Must have
• Keep the logo. In the US the company is called Dario Kellner Executive Search.

```html
<!DOCTYPE html>
<html lang="en">
<head>
<meta charset="utf-8">
<title>Dario Kellner Executive Search – Business Card</title>
<link rel="stylesheet" href="https://fonts.googleapis.com/css2?family=Questrial&display=swap">
<style>
  :root {
    --page: #e6eaea;
    --card: #ffffff;
    --mint: #5fd9b8;
    --mint-soft: #bff3e2;
    --mint-faint: #c9f3e6;
    --navy: #2d3b6b;
    --ink: #1e2230;
    --alert: #e0262b;
  }
  * { box-sizing: border-box; margin: 0; padding: 0; }
  html, body {
    width: 1200px; height: 741px; overflow: hidden;
    background: var(--page);
    font-family: "Questrial", "Century Gothic", sans-serif;
  }
  .card {
    position: absolute; left: 50px; top: 50px;
    width: 1100px; height: 641px;
    background: var(--card);
    box-shadow: 0 6px 24px rgba(0,0,0,.12);
  }
  .brand {
    position: absolute; right: 28px; top: 78px;
    display: flex; align-items: center; gap: 16px;
  }
  .brand-dot { width: 44px; height: 44px; border-radius: 50%; background: var(--mint); }
  .brand-name { font-size: 42px; color: var(--navy); white-space: nowrap; }
  .band-tab { position: absolute; left: 0; top: 192px; width: 41px; height: 105px; background: var(--mint-soft); }
  .band-fill { position: absolute; left: 480px; top: 192px; width: 620px; height: 105px; background: var(--mint-soft); }
  .person-name {
    position: absolute; left: 58px; top: 192px;
    font-size: 42px; font-weight: 400; color: var(--mint); white-space: nowrap;
  }
  .phone {
    position: absolute; left: 58px; top: 256px;
    display: flex; align-items: center; gap: 12px;
    font-size: 35px; color: var(--ink); white-space: nowrap;
  }
  .phone svg { width: 28px; height: 28px; }
  .contacts { position: absolute; left: 488px; top: 354px; list-style: none; }
  .contacts li {
    display: flex; align-items: flex-start; gap: 30px;
    font-size: 27px; line-height: 37px; color: var(--ink);
    margin-bottom: 8px; white-space: nowrap;
  }
  .contacts svg { width: 34px; height: 34px; flex: none; margin-top: 2px; }
  .footer {
    position: absolute; left: 8px; right: 8px; top: 582px;
    display: flex; align-items: center; gap: 10px;
    color: var(--mint-faint); font-size: 41px; letter-spacing: 1px; white-space: nowrap;
  }
  .footer::before, .footer::after { content: ""; flex: 1; height: 2px; background: var(--mint-faint); }
</style>
</head>
<body>
<main class="card">
  <div class="brand">
    <span class="brand-dot" aria-hidden="true"></span>
    <span class="brand-name">Dario Kellner</span>
  </div>

  <div class="band-tab"></div>
  <div class="band-fill"></div>

  <h1 class="person-name">Gustavo S. Kellner</h1>
  <p class="phone">
    <svg viewBox="0 0 24 24" aria-hidden="true"><path fill="var(--alert)" d="M6.6 2.5l3 3.2-1.8 2.6c1.2 2.9 3.2 5 6 6.3l2.6-1.8 3.2 3-2.3 3.2C10 18.6 5.2 13.8 3.2 4.8z"/></svg>
    555 014-0199
  </p>

  <ul class="contacts">
    <li>
      <svg viewBox="0 0 24 24" aria-hidden="true"><path fill="var(--mint)" d="M12 3l10 9h-3v9h-5v-6h-4v6H5v-9H2z"/></svg>
      <span>4820 Harbor Point Ave Suite 200<br>Bayview FL 33100</span>
    </li>
    <li>
      <svg viewBox="0 0 24 24" aria-hidden="true"><rect x="2" y="5" width="20" height="14" fill="var(--mint)"/><path d="M2 5l10 8 10-8" fill="none" stroke="#fff" stroke-width="1.8"/></svg>
      <span>www.dkexecutivesearch.com</span>
    </li>
    <li>
      <svg viewBox="0 0 24 24" aria-hidden="true"><circle cx="12" cy="12" r="10" fill="var(--mint)"/><path d="M2 12h20M12 2c-4 5-4 15 0 20M12 2c4 5 4 15 0 20" fill="none" stroke="#fff" stroke-width="1.4"/></svg>
      <span>gkellner@dkexecutivesearch.com</span>
    </li>
  </ul>

  <footer class="footer">Dario Kellner Executive Search</footer>
</main>
</body>
</html>
```